Help develop the "Breezy Brew" Logo & Can Design for new beer!

We're a new beer being produced in the Caribbean. Thus looking for a beer logo design that
1) capitalizes on the word "Breezy" for further beer lines that spin off of this first one. EXAMPLES OF OTHER BEER NAMES TO BE PRODUCED THAT HAVE TO HAVE TIE IN TO ORIGINAL DESIGN: "One Breezy Brew", "Sunny Pelican Wobble Brew" "Ramblefoot Breezy Brew" "Wharrya doin' Breezy Brew" "Bout now for Breezy Brew", "Tamarna Breezy Brew" etc etc etc,

2) has unique visual impact,
3) Logo has to be usable across variety of mediums,
4) 4 color maximum,
5) Island art feel,
6) Breezy Brew needs to convey a since of "lightness and slight tongue-in-cheek or off beat humor"...but not overwhelming,
7) Each subsequent label names (see above) needs to be distinctly color coded, but connects to the overarching theme of the brand with distinctive interpretations of each beer’s name.
8) Needs to be BOLD in statement and color.

You can get inspiration from some of these logo's. Follow this link: http://www.quorvelstudio.com/vintage-logos/
or http://www.tindralcrate.com/2014/12/30-beers-for-30-years-2001-to-2006.html

Also see attached files for inspiration!!!

Reason: We've extended the deadline for this project! Thus submit any new designs sooner than later. Thanks!

Target Market(s)

Male: Wear jeans & baseball cap, Played H.S. sports, Hunts/fish/golfDrive a truck or SUV, Work a blue collar job, Like working in the garage or on the landLike football/basketball/baseball, Are married high school sweetheart and have childrenAre from southern states...or wished they were, Chews tobacco or smokeDrink beerFemale: Attended college/community collegeAre married with kidsRide motorcycles, 4x4, ATV’sDrive Trucks or vansFish/camp/garden/sewDo craftsDrink beerGets manicures/pedicuresWears jewelry & jeans

Logo Text

Breezy Brew

Logo styles of interest
Emblem Logo
Pictorial/Combination Logo
Abstract Logo
Character Logo
Wordmark Logo
Requirements
Must have
• Eye catching & readable shelf presentation. Non-Standard art. High definition. Bold Statement. Clear design elements, various color options, High color contrast (like attached files) are needed for visual impact. Simple elements that conveys essence of the brand.
• You are designing the whole "beer can" logo elements, not just the the main logo. Things like background and side panels. Back panel for ingredients and messages to be added to. This is an "overall" can design, not just a single logo design.
• MUST HAVE THESE WORDS/SENTENCES/SECTIONS:
• Sentences: Our Breezy ales and lagers are handcrafted with some of the best ingredients the Caribbean has to offer!
• Section: So, Why Do we use can's?
• Can's eliminate potential light damage, reduce the risk of oxidation are lighter and chill quicker. Can be enjoyed on beaches and make for great recycling and table art. Plus they are the most recycled and eco-friendly material we can use. Breezy!
• BREWED AND BOTTLED/PACKED BY:
• IMPORTED BY
• ALCOHOL (ALC) ______% BY VOLUME (VOL)
• Recyclable
• GOVERNMENT WARNING:
• (1) According to the Surgeon General, women should not drink alcoholic beverages during pregnancy because of the risk of birth defects. (2) Consumption of
• alcoholic beverages impairs your ability to drive a car or operate machinery, and may cause health problems.
• Description: (This will change from beer to beer but this is good example of type language we would be using. "This Breezy Brew has a pletheria of Island goodness (there are hints of passion fruit, mango, and pineapple) along with some pleasant bitterness IPAs are known for. We can honestly say these sweet and savory flavors pair perfectly with this beer and you'll get a kick out of the IPA notes too!"
Should not have
• nudity, graphic language, skulls, flames,

```html
<!DOCTYPE html>
<html lang="en">
<head>
<meta charset="UTF-8">
<title>Breezy Brew – Can Label</title>
<link href="https://fonts.googleapis.com/css2?family=Montserrat:wght@400;600;700&family=Josefin+Sans:wght@400;600&display=swap" rel="stylesheet">
<style>
  :root {
    --stage: #eef2f5;
    --label-white: #ffffff;
    --sea-blue: #2fa8e0;
    --sea-blue-light: #8fd6f4;
    --deep-ink: #3a3f47;
    --soft-ink: #6b717a;
    --sun-yellow: #f5c21a;
    --sun-yellow-light: #fbe27a;
  }
  * { box-sizing: border-box; margin: 0; padding: 0; }
  html, body { width: 1200px; height: 716px; overflow: hidden; }
  body {
    background: var(--stage);
    font-family: "Montserrat", sans-serif;
    color: var(--deep-ink);
  }
  .label-sheet {
    position: relative;
    width: 1200px;
    height: 716px;
    display: flex;
    justify-content: center;
    align-items: center;
    gap: 48px;
  }
  .label-panel {
    position: relative;
    width: 330px;
    height: 580px;
    background: var(--label-white);
    border-radius: 6px;
    overflow: hidden;
    box-shadow: 0 6px 24px rgba(40, 60, 80, 0.14);
  }
  .sea-band {
    position: absolute; left: 0; top: 0; width: 100%; height: 72px;
    background: linear-gradient(180deg, var(--sea-blue) 0%, var(--sea-blue) 60%, var(--sea-blue-light) 100%);
  }
  .sun-band {
    position: absolute; left: 0; bottom: 0; width: 100%; height: 84px;
    background: linear-gradient(180deg, var(--sun-yellow-light), var(--sun-yellow));
  }
  /* Front panel */
  .since-line {
    position: absolute; top: 118px; left: 0; width: 100%;
    text-align: center;
    font-family: "Josefin Sans", sans-serif;
    font-size: 13px; letter-spacing: 6px; color: var(--deep-ink);
  }
  .hop-art {
    position: absolute; top: 150px; left: 70px;
    width: 190px; height: 150px;
    border-radius: 50% 50% 46% 46%;
    background: radial-gradient(circle at 40% 45%, var(--sun-yellow-light), var(--sun-yellow) 60%, var(--sea-blue-light) 100%);
  }
  .brand-name {
    position: absolute; top: 330px; left: 0; width: 100%;
    text-align: center;
    font-family: "Montserrat", sans-serif;
    font-weight: 700; font-size: 34px; line-height: 1.05;
    letter-spacing: 6px; color: var(--deep-ink);
  }
  .abv {
    position: absolute; top: 420px; left: 0; width: 100%;
    text-align: center; font-size: 13px; font-weight: 600; letter-spacing: 2px;
  }
  .volume {
    position: absolute; top: 442px; left: 0; width: 100%;
    text-align: center; font-size: 12px; letter-spacing: 2px; color: var(--soft-ink);
  }
  /* Back panel */
  .back-copy { position: absolute; top: 112px; left: 26px; width: 236px; }
  .intro-line {
    font-size: 11px; font-weight: 700; line-height: 1.45;
    text-transform: uppercase; letter-spacing: 0.5px; color: var(--deep-ink);
  }
  .star-row { margin: 12px 0 10px; display: flex; gap: 10px; justify-content: center; }
  .star-row svg { width: 12px; height: 12px; fill: var(--soft-ink); }
  .why-heading {
    font-size: 11px; font-weight: 700; text-transform: uppercase;
    color: var(--sea-blue); margin-bottom: 6px; letter-spacing: 0.5px;
  }
  .why-text {
    font-size: 10px; font-weight: 600; line-height: 1.5;
    text-transform: uppercase; color: var(--sea-blue);
  }
  .legal-text { margin-top: 12px; font-size: 7px; line-height: 1.4; color: var(--soft-ink); }
  .side-legal {
    position: absolute; top: 116px; right: 14px; height: 360px;
    writing-mode: vertical-rl;
    font-size: 10px; font-weight: 600; letter-spacing: 0.5px;
    text-transform: uppercase; color: var(--deep-ink); line-height: 1.7;
  }
  .recycle-mark {
    position: absolute; bottom: 104px; left: 26px;
    font-size: 9px; font-weight: 700; letter-spacing: 1px; color: var(--soft-ink);
    display: flex; align-items: center; gap: 6px;
  }
  .recycle-mark .dot { width: 10px; height: 10px; border-radius: 50%; border: 2px solid var(--soft-ink); display: inline-block; }
</style>
</head>
<body>
<main class="label-sheet">

  <section class="label-panel label-front">
    <div class="sea-band" role="img" aria-label="Decorative blue sea wave band with water droplets"></div>
    <p class="since-line">SINCE 2015</p>
    <div class="hop-art" role="img" aria-label="Illustration of two golden hop cones with green leaves"></div>
    <h1 class="brand-name">BREEZY<br>BREW</h1>
    <p class="abv">4.6% ALC VOL</p>
    <p class="volume">12 OZ · 0.35L</p>
    <div class="sun-band" role="img" aria-label="Golden band of rising beer bubbles"></div>
  </section>

  <section class="label-panel label-back">
    <div class="sea-band" role="img" aria-label="Decorative blue sea wave band with water droplets"></div>
    <div class="back-copy">
      <p class="intro-line">Our Breezy ales and lagers are handcrafted with some of the best ingredients the Caribbean has to offer!</p>
      <div class="star-row" aria-hidden="true">
        <svg viewBox="0 0 24 24"><path d="M12 2l3 7 7 .6-5.3 4.7 1.6 7.2L12 17.8 5.7 21.5l1.6-7.2L2 9.6 9 9z"/></svg>
        <svg viewBox="0 0 24 24"><path d="M12 2l3 7 7 .6-5.3 4.7 1.6 7.2L12 17.8 5.7 21.5l1.6-7.2L2 9.6 9 9z"/></svg>
        <svg viewBox="0 0 24 24"><path d="M12 2l3 7 7 .6-5.3 4.7 1.6 7.2L12 17.8 5.7 21.5l1.6-7.2L2 9.6 9 9z"/></svg>
      </div>
      <h2 class="why-heading">So, why do we use can's?</h2>
      <p class="why-text">Can's eliminate potential light damage, reduce the risk of oxidation, are lighter and chill quicker. Can be enjoyed on beaches and make for great recycling and table art. Plus they are the most recycled and eco-friendly material we can use. Breezy!</p>
      <p class="legal-text">GOVERNMENT WARNING: (1) According to the Surgeon General, women should not drink alcoholic beverages during pregnancy because of the risk of birth defects. (2) Consumption of alcoholic beverages impairs your ability to drive a car or operate machinery, and may cause health problems.</p>
    </div>
    <p class="side-legal">Brewed and bottled/packed by:<br>Imported by:</p>
    <p class="recycle-mark"><span class="dot"></span>RECYCLABLE</p>
    <div class="sun-band" role="img" aria-label="Golden band of rising beer bubbles"></div>
  </section>

</main>
</body>
</html>
```